We do the same thing as http://quarrytrades.com. We are called harborbets.com. Need a fast loading website which targets the same demographics as quarrytrades.com. That means a website that is full of energy and excitement, capture concepts of volcano, explosiveness and profit.

Use all content from their site as placeholder.

```html
<!DOCTYPE html>
<html lang="en">
<head>
<meta charset="utf-8">
<title>Harbor Bets – Free Penny Stock Alerts</title>
<link rel="stylesheet" href="https://fonts.googleapis.com/css2?family=Anton&family=Open+Sans:wght@400;600;700&family=Kaushan+Script&display=swap">
<style>
:root{
  --black:#000;
  --panel:#17110c;
  --panel-edge:#3a2d22;
  --pill:#0c0a08;
  --gold:#ffd24a;
  --orange:#ff8a00;
  --red:#e00000;
  --yellow:#ffe600;
  --title-yellow:#f5de3f;
  --copy-brown:#9a6840;
  --white:#fff;
  --input:#1f1712;
  --tick:#3fcf2a;
}
*{margin:0;padding:0;box-sizing:border-box}
html,body{width:900px;height:1200px;overflow:hidden;background:var(--black)}
body{position:relative;font-family:'Open Sans',Arial,sans-serif;color:var(--white)}
.hero-glow{position:absolute;left:0;top:0;width:900px;height:380px;
  background:radial-gradient(ellipse 420px 120px at 640px 150px,rgba(190,20,30,.55),transparent 70%),
  radial-gradient(ellipse 260px 80px at 760px 100px,rgba(255,120,60,.35),transparent 70%),
  linear-gradient(#0a0a10,#000)}
.brand{position:absolute;left:36px;top:62px;display:flex;align-items:center;gap:10px;
  font-family:'Anton',sans-serif;font-size:44px;color:var(--gold);letter-spacing:1px}
.brand-dot{width:16px;height:16px;border-radius:50%;background:var(--orange)}
.tagline{position:absolute;left:296px;top:78px;font-family:'Kaushan Script',cursive;font-size:26px;color:var(--white);white-space:nowrap}
.tagline .hot{color:var(--red);font-size:34px}
.tagline .gold{color:var(--gold);font-size:34px}
.cta-badge{position:absolute;left:40px;top:169px;width:230px;height:73px;border:2px solid #fff;border-radius:8px;
  background:linear-gradient(#ffae00,#e84800 60%,#c82000);padding:10px 0 0 18px;
  font-weight:700;font-size:19px;line-height:27px;color:var(--black);text-shadow:0 0 2px #fff}
.cta-badge .free{color:var(--red)}
.perks{position:absolute;left:290px;top:165px;list-style:none;font-size:15px;font-weight:600;line-height:27px}
.perks li{display:flex;align-items:center;gap:8px}
.perks svg{width:15px;height:13px}
.signup{position:absolute;display:flex;gap:3px}
.signup .email{width:578px;height:33px;background:var(--input);border:1px solid #8a7a6a;color:#aaa;font-size:15px;padding:5px 16px}
.signup .btn{width:121px;height:34px;border:1px solid #fff;background:linear-gradient(#ff2a00,#900);
  color:var(--yellow);font-weight:700;font-size:20px;text-align:center;line-height:32px}
.signup.top{left:107px;top:292px}
.signup.bottom{left:108px;top:1085px}
.ticker{position:absolute;top:364px;width:190px;height:165px;background:var(--panel);border:1px solid var(--panel-edge);text-align:center}
.ticker .sym{font-family:'Anton',sans-serif;font-size:68px;line-height:1;margin-top:8px;
  background:linear-gradient(#ffe060,#ff8a00);-webkit-background-clip:text;background-clip:text;color:transparent;letter-spacing:2px}
.ticker .gain{margin:18px auto 0;width:150px;height:47px;border-radius:5px;background:var(--pill);font-size:20px;line-height:47px}
.welcome{position:absolute;left:62px;top:556px;font-size:27px}
.welcome small{font-size:18px}
.intro{position:absolute;left:60px;top:603px;width:790px;font-family:Arial,sans-serif;font-size:12.5px;line-height:15.5px;color:var(--copy-brown)}
.features{position:absolute;left:42px;top:681px;width:813px;height:254px;background:var(--panel);border:1px solid var(--panel-edge);display:flex}
.feature{flex:1;padding:18px 0 0 18px;border-right:1px solid #2a2018}
.feature:last-child{border-right:0}
.feature h3{font-size:19px;font-weight:600;line-height:26px;color:var(--title-yellow);height:56px}
.feature .art{width:227px;height:73px;margin-top:6px}
.feature p{margin-top:13px;font-family:Arial,sans-serif;font-size:12.5px;line-height:15px;color:var(--copy-brown);width:225px}
.feature .more{display:block;margin-top:8px;font-size:10px;font-weight:700;color:var(--yellow)}
.art-disco{background:linear-gradient(90deg,#d0103a,#a0206a 40%,#1a8030 70%,#20c0c0)}
.art-green{background:linear-gradient(90deg,#0a5a20,#16a050 50%,#20c8a8)}
.art-red{background:linear-gradient(90deg,#8a0008,#e02010 50%,#f06020)}
.footer-zone{position:absolute;left:0;top:958px;width:900px;height:242px;background:var(--yellow)}
.flames{position:absolute;left:0;top:0;width:900px;height:72px;background:linear-gradient(#000 0%,#c83000 30%,#ff8a00 65%,var(--yellow))}
.footer-title{position:absolute;left:0;width:900px;top:76px;text-align:center;font-family:'Kaushan Script',cursive;font-size:36px;color:var(--white);
  -webkit-text-stroke:1.5px #000;white-space:nowrap}
.footer-title .red{color:var(--red)}
.rule{position:absolute;left:38px;top:173px;width:820px;height:1px;background:#8a7a00}
.legal{position:absolute;left:0;top:182px;width:900px;text-align:center;font-size:12px;line-height:15.5px;color:#000}
</style>
</head>
<body>
<div class="hero-glow" role="img" aria-label="Dark starry sky with sweeping red light streaks"></div>

<div class="brand"><span class="brand-dot"></span>HARBOR BETS</div>
<div class="tagline">Receive <span class="hot">Hot</span> penny stock <span class="gold">Alearts</span> for <span class="hot">Free!</span></div>

<div class="cta-badge">SIGN UP for <span class="free">FREE</span><br>Penny stock ALERTS!</div>
<ul class="perks">
  <li><svg viewBox="0 0 15 13"><path d="M1 7l4 4L14 1" fill="none" stroke="#3fcf2a" stroke-width="3"/></svg>Join the Most Explosive Penny Stock Newsletter on the WEB ... 100% FREE</li>
  <li><svg viewBox="0 0 15 13"><path d="M1 7l4 4L14 1" fill="none" stroke="#3fcf2a" stroke-width="3"/></svg>HOT Penny Stock Alerts Delivered Directly to your Email</li>
  <li><svg viewBox="0 0 15 13"><path d="M1 7l4 4L14 1" fill="none" stroke="#3fcf2a" stroke-width="3"/></svg>Don't hesitate! There are LIMITED spots available.</li>
</ul>

<div class="signup top"><div class="email">Enter your email here....</div><div class="btn">SIGN UP</div></div>

<div class="ticker" style="left:42px"><div class="sym">QRLX</div><div class="gain">840% Gain</div></div>
<div class="ticker" style="left:250px"><div class="sym">TPHV</div><div class="gain">840% Gain</div></div>
<div class="ticker" style="left:458px"><div class="sym">KLDR</div><div class="gain">840% Gain</div></div>
<div class="ticker" style="left:665px"><div class="sym">VNTQ</div><div class="gain">840% Gain</div></div>

<h1 class="welcome">Welcome <small>Harbor Bets home page</small></h1>
<p class="intro">Lorem Ipsum is simply dummy text of the printing and typesetting industry. Lorem Ipsum has been the industry's standard dummy text ever since the 1500s, when an unknown printer took a galley of type and scrambled it to make a type specimen book. It has survived not only five centuries, but also the leap into electronic typesetting,</p>

<section class="features">
  <article class="feature">
    <h3>FREE DAILY PENNY<br>STOCKS PICKS</h3>
    <div class="art art-disco" role="img" aria-label="Colourful disco ball with green and cyan bokeh"></div>
    <p>Our newsletters are completely FREE. We do not charge anything to our sub-scribers. Feel free to share our website with your family &amp; friends.</p>
    <span class="more">KNOW MORE...</span>
  </article>
  <article class="feature">
    <h3>HARBOR<br>STOCK PICKS!!!</h3>
    <div class="art art-green" role="img" aria-label="Green abstract bokeh circles"></div>
    <p>Our newsletters are completely FREE. We do not charge anything to our sub-scribers. Feel free to share our website with your family &amp; friends.</p>
    <span class="more">KNOW MORE...</span>
  </article>
  <article class="feature">
    <h3>FREE<br>STOCK ALERTS</h3>
    <div class="art art-red" role="img" aria-label="Red and orange abstract bokeh shapes"></div>
    <p>Our newsletters are completely FREE. We do not charge anything to our sub-scribers. Feel free to share our website with your family &amp; friends.</p>
    <span class="more">KNOW MORE...</span>
  </article>
</section>

<footer class="footer-zone">
  <div class="flames" role="img" aria-label="Row of orange flames rising into the yellow footer"></div>
  <div class="footer-title">Sign up for <span class="red">Free</span> Penny stock <span class="red">Newsletter!</span></div>
  <div class="rule"></div>
  <div class="legal">100% Anti-Spam &amp; will never rent or sell your information!<br>Unsubscribe at any time simply by clicking a link found at the bottom of any email you receive from us.<br>Privacy Policy | Disclaimer</div>
</footer>
<div class="signup bottom"><div class="email">Enter your email here....</div><div class="btn">SIGN UP</div></div>
</body>
</html>
```